Jolly Paws Business Card Update

I have a business card which I love. I want to keep the same logo, colours, font and style. I want to upgrade the scripting and remove some elements and add others.
On the front side under Services - remove the existing wording and insert - Providing individual coaching strategies to create happy, healthy and social canine companions
Under Rebecca Thornbury amend the current wording to read: Qualified in Dog Behavioural Training, Natural Animal Healthcare and Animal Health Science
On the reverse side to remove the web address.

```html
<!DOCTYPE html>
<html lang="en">
<head>
<meta charset="utf-8">
<title>Jolly Paws Business Card</title>
<link rel="stylesheet" href="https://fonts.googleapis.com/css2?family=Arimo:wght@400;700&display=swap">
<style>
  :root {
    --backdrop: #2c2c2c;
    --blue-top: #0590cf;
    --blue-mid: #1f63b0;
    --blue-deep: #2b357e;
    --red-bright: #d11c22;
    --red-deep: #6e1a1c;
    --cream: #e9e2cd;
    --cream-dark: #d6cdb2;
    --ink: #1a1a1a;
    --white: #f4f4f6;
  }
  * { box-sizing: border-box; margin: 0; padding: 0; }
  html, body {
    width: 1200px; height: 1138px; overflow: hidden;
    background: var(--backdrop);
    font-family: "Arimo", Arial, sans-serif;
  }
  .card {
    position: absolute;
    border-radius: 14px;
    overflow: hidden;
    box-shadow: 0 4px 10px rgba(0,0,0,.45);
  }
  .card--front {
    left: 274px; top: 186px; width: 623px; height: 376px;
    background: linear-gradient(180deg, var(--blue-top) 0%, var(--blue-mid) 55%, var(--blue-deep) 100%);
  }
  .card--back {
    left: 276px; top: 608px; width: 618px; height: 374px;
  }
  .brand-disc {
    position: absolute;
    border-radius: 50%;
    background: var(--cream);
  }
  .card--front .brand-disc {
    left: 251px; top: 78px; width: 120px; height: 120px;
  }
  .brand-name {
    position: absolute; left: 0; right: 0; top: 226px;
    text-align: center;
    font-size: 38px; font-weight: 700; letter-spacing: 1px;
    color: var(--white);
  }
  .tagline {
    position: absolute; left: 0; right: 0; top: 275px;
    text-align: center;
    font-size: 19px; color: var(--white);
  }
  .back-upper {
    position: absolute; left: 0; top: 0; width: 100%; height: 213px;
    background: linear-gradient(180deg, var(--blue-top) 0%, var(--blue-top) 35%, var(--blue-mid) 100%);
  }
  .card--back .brand-disc {
    left: 86px; top: 58px; width: 100px; height: 100px;
  }
  .back-brand {
    position: absolute; left: 36px; top: 170px; width: 200px;
    text-align: center;
    font-size: 17px; font-weight: 700; color: var(--white);
  }
  .services-title {
    position: absolute; left: 246px; top: 72px;
    font-size: 19px; color: var(--white);
  }
  .services-text {
    position: absolute; left: 246px; top: 112px; width: 290px;
    font-size: 15.5px; line-height: 19px; color: var(--white);
  }
  .mission-band {
    position: absolute; left: 0; top: 213px; width: 100%; height: 23px;
    background: linear-gradient(90deg, var(--cream-dark), var(--cream) 50%, var(--cream-dark));
    text-align: center;
    font-size: 15.5px; line-height: 23px; color: var(--ink);
  }
  .back-lower {
    position: absolute; left: 0; top: 236px; width: 100%; height: 138px;
    background: radial-gradient(ellipse 60% 140% at 48% 20%, var(--red-bright) 0%, #a51c20 45%, var(--red-deep) 100%);
  }
  .person {
    position: absolute; right: 292px; top: 36px; width: 320px;
    text-align: right; color: var(--white);
  }
  .person-name { font-size: 22px; margin-bottom: 5px; }
  .person-role { font-size: 13.5px; line-height: 17px; }
  .contacts {
    position: absolute; left: 345px; top: 60px;
    list-style: none; color: var(--white);
    font-size: 19px;
  }
  .contacts li { display: flex; align-items: center; height: 24px; }
  .contacts svg { width: 16px; height: 16px; margin-right: 8px; flex: none; }
</style>
</head>
<body>
  <section class="card card--front" aria-label="Card front">
    <div class="brand-disc"></div>
    <div class="brand-name">JOLLY PAWS</div>
    <div class="tagline">HAPPY DOGS, HAPPY OWNERS</div>
  </section>

  <section class="card card--back" aria-label="Card back">
    <div class="back-upper">
      <div class="brand-disc"></div>
      <div class="back-brand">JOLLY PAWS</div>
      <h2 class="services-title" style="font-weight:400">SERVICES</h2>
      <p class="services-text">Providing individual coaching strategies to create happy, healthy and social canine companions</p>
    </div>
    <div class="mission-band">Promoting communication and connection between dogs and their families</div>
    <div class="back-lower">
      <div class="person">
        <div class="person-name">Rebecca Thornbury</div>
        <div class="person-role">Qualified in Dog Behavioural Training, Natural Animal Healthcare and Animal Health Science</div>
      </div>
      <ul class="contacts">
        <li>
          <svg viewBox="0 0 16 16" aria-hidden="true"><circle cx="8" cy="8" r="7.5" fill="#f4f4f6"/><rect x="5.5" y="3.5" width="5" height="9" rx="1" fill="none" stroke="#8a1c1f" stroke-width="1.3"/></svg>
          0400 000 000
        </li>
        <li>
          <svg viewBox="0 0 16 16" aria-hidden="true"><circle cx="8" cy="8" r="7.5" fill="#f4f4f6"/><rect x="4" y="5" width="8" height="6" fill="none" stroke="#8a1c1f" stroke-width="1.3"/><path d="M4 5l4 3.5L12 5" fill="none" stroke="#8a1c1f" stroke-width="1.3"/></svg>
          hello@jollypaws.example
        </li>
      </ul>
    </div>
  </section>
</body>
</html>
```